Crowdsourced IT recruitment agency - velmorix

We need an engaging and smart website design for VELMORIX Crowd recruitment. We are young innovative IT recruitment company. We have deep expertise in all IT & digital areas and using crowdsourcing to search the best market candidates faster than ever.
Our mission: to connect people and organizations interests, inspiring each other and enabling together reach better results.

We would like the design to be personalized, emotional, yet simple and neat. It should focus on the person with a problem which we solve.

Reading the site customers should feel safe and confident that velmorix is the trusted partner and everything we do is a quality product.

We also focus on long term relationship with our clients.

We have 4 products:
IT Recruitment – professional recruitment of candidates in IT and digital areas
IT RPO – candidates research process outsourcing(RPO) - provision of resume pools for the client
Kestrel Talent School – training, seminars and networking events for HR professionals from IT and hi-tech companies
Plumview Board – a tool for data visualization in nice and interactive dashboards. It pulls data from different corporate sources (SAP, Oracle, excel, etc.). It looks like a dashboard, on which there are several graphs or diagrams with HR and business KPIs(key performance indicators)

We like material design sites but also open for other options/ideas

Current site velmorix-hire.ru

Examples of websites that we like:
http://www.quobrant.ru
https://dunmirecardio.ru

Site structure:
About us (description, mission, team, clients, office)
Products: Plumview Board, HR IPO, It Recruitment
Kestrel Talent School (list of events (past and future) with the ability to upload photos, descriptions, etc.)
News: Publications, Articles, Blog
Contacts

Industry/Entity Type

Consulting

Number of Pages Required

5+ page

Font styles to use
Serif
Sans Serif

Requirements
Must have
• Individual blocks with the transition to a separate page for each product
• Link to social network (fb, link),
• Subscribe to news on the main page
• Feedback form
• Site structure:
• About us (description, mission, team, clients, office)
• Products: Plumview Board, HR IPO, It Recruitment
• Kestrel Talent School (list of events (past and future) with the ability to upload photos, descriptions, etc.)
• News: Publications, Articles, Blog, Calendars
• Contacts
Should not have
• too crowded
• too complicatied
• without advertising banners
• crammed

```html
<!DOCTYPE html>
<html lang="en">
<head>
<meta charset="utf-8">
<title>VELMORIX Crowd recruitment</title>
<link href="https://fonts.googleapis.com/css2?family=Cinzel:wght@400;700&family=Open+Sans:wght@400;600;700&family=Poppins:wght@500;600;700&display=swap" rel="stylesheet">
<style>
:root{
  --navy:#1d4f8f;
  --blue:#1e5ba8;
  --cyan:#1ba3dd;
  --gold:#e8a40c;
  --ink:#333;
  --muted:#666;
  --line:#d6d6d6;
  --mist:#c9dbe5;
  --band:#e6e6e6;
  --footer:#222;
  --white:#fff;
}
*{box-sizing:border-box;margin:0;padding:0}
html,body{width:1200px;height:4009px;overflow:hidden}
body{font-family:"Open Sans",Arial,sans-serif;color:var(--ink);background:var(--white);position:relative}
.sec{position:absolute;left:0;width:1200px}
.abs{position:absolute}
.h2{font-family:"Poppins",Arial,sans-serif;font-weight:700;color:var(--navy);text-transform:uppercase;font-size:25px;letter-spacing:.5px}
.center{text-align:center;left:0;width:1200px}
.btn-grey{display:inline-block;background:#e2e2e2;border:1px solid #cfcfcf;font-size:12px;font-weight:600;padding:5px 14px;color:#444;text-transform:uppercase}
p{line-height:1.6}

/* header */
.header{top:0;height:72px;background:var(--white)}
.brand{left:70px;top:12px;display:flex;align-items:center;gap:10px}
.brand-dot{width:44px;height:44px;border-radius:50%;background:var(--navy)}
.brand-name{font-family:"Poppins",sans-serif;font-weight:600;font-size:24px;color:var(--navy);line-height:1}
.brand-sub{font-size:9px;color:var(--navy);letter-spacing:1px;text-transform:uppercase}
.nav{left:322px;top:26px;display:flex;gap:40px;font-family:"Poppins",sans-serif;font-weight:600;font-size:15px;color:#222}
.auth{right:75px;top:16px;display:flex;gap:6px}
.auth a{display:block;background:var(--cyan);color:#fff;font-weight:700;font-size:14px;padding:9px 18px;text-decoration:none}
.auth a.reg{background:var(--blue)}

/* hero */
.hero{top:72px;height:543px;background:linear-gradient(180deg,#c9c5c2 0%,#a59c96 45%,#6f6660 100%)}
.hero-title{top:352px;font-family:"Cinzel",serif;font-weight:700;font-size:44px;color:#fff;text-shadow:0 2px 6px rgba(0,0,0,.4)}
.hero-sub{top:408px;font-size:22px;color:#f1f1f1}
.hero-band{top:481px;left:0;width:1200px;height:56px;background:rgba(20,20,20,.72);color:#fff;font-size:16px;text-align:center;line-height:24px;padding-top:4px}

/* welcome */
.welcome{top:615px;height:419px}
.welcome-photo{left:75px;top:56px;width:510px;height:302px;background:linear-gradient(135deg,#e7eef3,#b9c4cc 60%,#6b5f8a)}
.welcome-text{left:615px;top:68px;width:510px}
.welcome-text .kicker{font-family:"Poppins",sans-serif;font-weight:700;font-size:14px;color:#222}
.welcome-text .h2{font-size:24px;margin-bottom:14px}
.welcome-text p{font-size:15px;margin-bottom:12px}

/* mission */
.mission{top:1034px;height:177px;background:var(--mist)}
.mission .h2{top:39px}
.mission p{top:76px;font-size:21px;color:#555;line-height:1.5}

/* products */
.products{top:1216px;height:475px}
.products .h2{top:46px}
.product{top:128px;width:250px;text-align:center}
.product .ring{width:144px;height:144px;border-radius:50%;border:2px solid #d9d9d9;margin:0 auto 26px;display:flex;align-items:center;justify-content:center}
.product h3{font-family:"Poppins",sans-serif;font-size:16px;color:#222;margin-bottom:14px;text-transform:uppercase}
.product p{font-size:14px;color:#555;margin-bottom:16px;height:46px;overflow:hidden}

/* features */
.features{top:1691px;height:290px;background:var(--band)}
.features .h2{top:48px;font-size:24px}
.features .lead{top:88px;font-size:15px;color:#555}
.feat{top:139px;width:226px;height:128px;background:#fff;text-align:center;padding-top:20px}
.feat h4{font-family:"Poppins",sans-serif;font-size:15px;color:var(--navy);margin:6px 0 4px}
.feat p{font-size:13px;color:#555;line-height:1.4;padding:0 14px}

/* how & events */
.how{top:1981px;height:563px}
.how .how-title{top:96px;left:75px;font-size:24px}
.how .lead{top:133px;left:75px;font-size:14px}
.video{left:75px;top:178px;width:510px;height:326px;background:linear-gradient(90deg,#6c7a84,#a9b3b9 50%,#5f6c75)}
.play{left:294px;top:305px}
.how .events-title{left:612px;top:96px;font-size:24px}
.event{left:612px;width:513px;height:94px}
.event .thumb{position:absolute;left:0;top:0;width:152px;height:94px}
.event .info{position:absolute;left:166px;top:0;font-size:13px}
.event .date{font-weight:600;font-size:12px}
.event h5{font-size:15px;font-weight:700;margin:2px 0 6px}
.event p{line-height:1.5;color:#555}

/* articles */
.articles{top:2544px;height:556px;background:#e8e8e8}
.articles .h2{top:48px}
.article{top:109px;width:330px;height:374px;padding:24px 26px;color:#fff}
.article.active{outline:8px solid var(--blue);outline-offset:-8px}
.article h3{font-family:"Poppins",sans-serif;font-weight:700;font-size:24px;line-height:1.2}
.article .date{position:absolute;left:26px;bottom:18px;font-size:13px}

/* testimonials */
.testimonials{top:3100px;height:529px}
.testimonials .h2{top:40px}
.t-rule{top:56px;height:1px;background:#e2e2e2}
.quote{width:320px;background:#eeeeee;padding:18px 20px;font-size:14px;color:#555;line-height:1.55;box-shadow:0 2px 3px rgba(0,0,0,.15)}
.who{display:flex;align-items:center;gap:12px;font-weight:700;font-size:15px;color:#333}
.avatar{width:44px;height:44px;border-radius:50%;background:#d4d4d4;border:3px solid #fff}

/* footer */
.footer{top:3629px;height:380px;background:var(--footer);color:#eee;font-size:13px}
.footer h6{font-size:14px;font-weight:700;text-transform:uppercase;margin-bottom:14px}
.footer ul{list-style:none;line-height:1.75}
.f-input{width:284px;height:36px;background:#fff;color:#888;font-size:14px;padding:8px 10px;margin-bottom:8px}
.f-btn{display:inline-block;background:var(--gold);color:#222;font-weight:700;font-size:13px;padding:9px 16px;text-transform:uppercase}
.feedback{left:795px;top:-13px;width:336px;height:372px;background:var(--blue);border:4px solid #3b7ccf;padding:26px 24px}
.feedback h6{font-family:"Poppins",sans-serif;font-size:20px;margin:0 0 18px 38px}
.feedback .f-input{width:100%}
.social{display:flex;gap:10px;align-items:center}
.social span{width:34px;height:34px;border-radius:50%;border:2px solid #ddd;display:block}
</style>
</head>
<body>

<header class="sec header">
  <div class="abs brand"><span class="brand-dot"></span><div><div class="brand-name">velmorix</div><div class="brand-sub">crowd recruitment</div></div></div>
  <nav class="abs nav"><span>HOME</span><span>ABOUT US</span><span>PRODUCTS</span><span>NEWS</span><span>CONTACTS</span></nav>
  <div class="abs auth"><a href="#">LOG IN</a><a class="reg" href="#">REGISTER</a></div>
</header>

<section class="sec hero" role="img" aria-label="Smiling group of professionals in an office">
  <h1 class="abs center hero-title" style="text-align:center">GET YOUR PERFECT IT CANDIDATES</h1>
  <p class="abs center hero-sub" style="text-align:center">More Recruiters. Better Candidates. Lower Costs.</p>
  <div class="abs hero-band">Hiring has never been easier. Staff your teams faster with the first crowdsourced IT recruitment agency. Over 150 professional recruiters<br>ready to work on your project. Welcome to velmorix!</div>
</section>

<section class="sec welcome">
  <div class="abs welcome-photo" role="img" aria-label="Businesswoman seated on a purple sofa in a bright office"></div>
  <div class="abs welcome-text">
    <div class="kicker">WELCOME TO</div>
    <div class="h2">VELMORIX Crowd recruitment</div>
    <p>Lorem ipsum dolor sit amet, consectetur adipisicing elit, sed do eiusmod tempor incididunt ut labore et dolore magna aliqua. Ut enim ad minim veniam, quis nostrud exercitation ullamco laboris nisi ut aliquip ex ea commodo consequat. Duis aute irure dolor in reprehenderit in voluptate velit esse. magna aliqua. Ut enim ad minim veniam, quis nostrud exercitation ullamco laboris nisi ut aliquip ex ea commodo consequat.</p>
    <span class="btn-grey">Read more</span>
  </div>
</section>

<section class="sec mission">
  <div class="abs center h2" style="text-align:center">Our mission</div>
  <p class="abs center" style="text-align:center">To connect people and organizations interests, inspiring each other and<br>enabling together reach better results.</p>
</section>

<section class="sec products">
  <div class="abs center h2" style="text-align:center">Our products</div>
  <div class="abs product" style="left:73px">
    <div class="ring"><svg width="70" height="70" viewBox="0 0 70 70" fill="none" stroke="#333" stroke-width="2"><circle cx="35" cy="28" r="16"/><circle cx="35" cy="24" r="5"/><path d="M27 36c2-5 14-5 16 0"/><path d="M14 58c3-8 9-10 12-10M56 58c-3-8-9-10-12-10"/><circle cx="16" cy="42" r="4"/><circle cx="54" cy="42" r="4"/></svg></div>
    <h3>IT Recruitment</h3>
    <p>Professional recruitment of candidates in IT and digital areas...</p>
    <span class="btn-grey">Read more</span>
  </div>
  <div class="abs product" style="left:340px">
    <div class="ring"><svg width="70" height="70" viewBox="0 0 70 70" fill="none" stroke="#333" stroke-width="2"><path d="M35 24l12 6-12 6-12-6z"/><path d="M27 34v6c4 3 12 3 16 0v-6"/><circle cx="35" cy="8" r="4"/><circle cx="10" cy="35" r="4"/><circle cx="60" cy="35" r="4"/><circle cx="35" cy="62" r="4"/><path d="M35 12v12M14 35h9M47 35h9M35 46v12"/></svg></div>
    <h3>IT RPO</h3>
    <p>Candidates research process out-sourcing(RPO) - provision...</p>
    <span class="btn-grey">Read more</span>
  </div>
  <div class="abs product" style="left:610px">
    <div class="ring"><svg width="70" height="70" viewBox="0 0 70 70" fill="none" stroke="#333" stroke-width="2"><circle cx="35" cy="16" r="6"/><circle cx="16" cy="26" r="5"/><circle cx="54" cy="26" r="5"/><path d="M25 34c0-6 20-6 20 0M8 40c0-5 14-5 14 0M48 40c0-5 14-5 14 0"/><circle cx="35" cy="52" r="8"/><path d="M35 40v4M35 60v4M23 52h4M43 52h4"/></svg></div>
    <h3>Kestrel Talent School</h3>
    <p>Training, seminars and networking events for HR professionals...</p>
    <span class="btn-grey">Read more</span>
  </div>
  <div class="abs product" style="left:880px">
    <div class="ring"><svg width="72" height="60" viewBox="0 0 72 60" fill="none" stroke="#333" stroke-width="2"><rect x="4" y="4" width="64" height="44"/><path d="M28 56h16M36 48v8"/><path d="M10 40V28M16 40V22M22 40V30"/><circle cx="38" cy="30" r="8"/><path d="M38 22v8h8"/><path d="M50 38l6-8 6 4"/><path d="M10 12h24"/></svg></div>
    <h3>Plumview Board</h3>
    <p>A tool for data visualization in nice and interactive dashboards...</p>
    <span class="btn-grey">Read more</span>
  </div>
</section>

<section class="sec features">
  <div class="abs center h2" style="text-align:center">VELMORIX is the first crowdsourced IT recruitment agency</div>
  <p class="abs center lead" style="text-align:center">We have deep and unique expertise in IT area using crowdsourcing to search the best market candidates faster than ever.</p>
  <div class="abs feat" style="left:118px"><svg width="26" height="26" viewBox="0 0 26 26" fill="none" stroke="#1d4f8f" stroke-width="2"><path d="M3 13h18M15 7l6 6-6 6"/></svg><h4>END-TO-END</h4><p>IT recruitment focused on result</p></div>
  <div class="abs feat" style="left:363px"><svg width="26" height="26" viewBox="0 0 26 26" fill="none" stroke="#1d4f8f" stroke-width="2"><path d="M4 14l6 6 12-14"/></svg><h4>EASY</h4><p>One point of contact to the recruiters crowd</p></div>
  <div class="abs feat" style="left:609px"><svg width="26" height="26" viewBox="0 0 26 26" fill="none" stroke="#1d4f8f" stroke-width="2"><path d="M5 4h16l4 6-12 14L1 10z M1 10h24 M9 4l4 20 4-20"/></svg><h4>QUALITY</h4><p>Broad and deep expertize in all IT areas</p></div>
  <div class="abs feat" style="left:858px"><svg width="26" height="26" viewBox="0 0 26 26" fill="none" stroke="#1d4f8f" stroke-width="2"><circle cx="13" cy="14" r="10"/><path d="M13 8v6l4 3M10 2h6"/></svg><h4>FASTER</h4><p>Network gives result in 3 days</p></div>
</section>

<section class="sec how">
  <div class="abs h2 how-title">How does it work?</div>
  <p class="abs lead">Watch this video to learn about our process and results you can expect.</p>
  <div class="abs video" role="img" aria-label="Video still of a smiling recruiter in an office"></div>
  <svg class="abs play" width="72" height="72" viewBox="0 0 72 72" fill="none"><circle cx="36" cy="36" r="33" stroke="#fff" stroke-width="4"/><path d="M28 22l22 14-22 14z" fill="#fff"/></svg>

  <div class="abs h2 events-title">Upcoming events</div>
  <div class="abs event" style="top:143px"><div class="thumb" role="img" aria-label="Business people shaking hands" style="background:linear-gradient(135deg,#8a7e6c,#3f3a35)"></div><div class="info"><div class="date">20 Mar, 2017</div><h5>Lorem ipsum dolor sit amet.</h5><p>Sed do eiusmod tempor incididunt ut labore et dolore<br>magna aliqua. Ut enim ad minim veniam.</p></div></div>
  <div class="abs event" style="top:277px"><div class="thumb" role="img" aria-label="Hands holding glowing network figures" style="background:linear-gradient(135deg,#0e2a52,#2f6fb8)"></div><div class="info"><div class="date">20 Mar, 2017</div><h5>Lorem ipsum dolor sit amet.</h5><p>Sed do eiusmod tempor incididunt ut labore et dolore<br>magna aliqua. Ut enim ad minim veniam.</p></div></div>
  <div class="abs event" style="top:410px"><div class="thumb" role="img" aria-label="Team meeting around a desk" style="background:linear-gradient(135deg,#d9dde0,#6f7d88)"></div><div class="info"><div class="date">20 Mar, 2017</div><h5>Lorem ipsum dolor sit amet.</h5><p>Sed do eiusmod tempor incididunt ut labore et dolore<br>magna aliqua. Ut enim ad minim veniam.</p></div></div>
  <div class="abs" style="left:612px;top:257px;width:513px;height:1px;background:var(--line)"></div>
  <div class="abs" style="left:612px;top:390px;width:513px;height:1px;background:var(--line)"></div>
</section>

<section class="sec articles">
  <div class="abs center h2" style="text-align:center">Articles</div>
  <article class="abs article" style="left:75px;background:linear-gradient(180deg,#3a3530,#8c8276)" role="img" aria-label="Wooden blocks with people symbols"><h3>Lorem ipsum dolor sit amet, consectetur adipiscing elit,</h3><span class="date">18 MAR, 2017</span></article>
  <article class="abs article active" style="left:436px;background:linear-gradient(180deg,#2b2f35,#4a5058)" role="img" aria-label="Dimly lit office workspace"><h3>Lorem ipsum dolor sit amet, consectetur adipiscing elit,</h3><span class="date">18 MAR, 2017</span></article>
  <article class="abs article" style="left:794px;background:linear-gradient(180deg,#5a5660,#7b6b76)" role="img" aria-label="Smiling woman at a desk"><h3>Lorem ipsum dolor sit amet, consectetur adipiscing elit,</h3><span class="date">18 MAR, 2017</span></article>
</section>

<section class="sec testimonials">
  <div class="abs t-rule" style="left:75px;width:360px"></div>
  <div class="abs t-rule" style="left:765px;width:360px"></div>
  <div class="abs center h2" style="text-align:center">Testimonial</div>
  <div class="abs" style="left:75px;top:116px">
    <div class="quote">“Lorem ipsum dolor sit amet, consectetur adipiscing elit, sed do eiusmod tempor incididunt ut labore et dolore magna aliqua. Ut enim ad minim veniam, quis nostrud exercitation ullamco laboris nisi ut aliquip ex ea commodo consequat. Duis aute irure dolor in reprehenderit”</div>
    <div class="who" style="margin:6px 0 0 30px"><span class="avatar"></span>Mr Doblin,</div>
  </div>
  <div class="abs" style="left:436px;top:116px">
    <div class="quote" style="width:330px">“Lorem ipsum dolor sit amet, consectetur adipiscing elit, sed do eiusmod tempor incididunt ut labore et dolore magna aliqua. Ut enim ad minim veniam, quis nostrud exercitation ullamco laboris nisi ut aliquip ex ea commodo consequat. Duis aute irure dolor in reprehenderit in voluptate velit esse cillum dolore eu fugiat nulla pariatur. Excepteur sint occaecat cupidatat non proident, sunt in culpa qui officia deserunt mollit”</div>
    <div class="who" style="margin:6px 0 0 30px"><span class="avatar"></span>Mr &amp; Mrs Fenwarth,</div>
  </div>
  <div class="abs" style="left:794px;top:116px">
    <div class="quote" style="width:330px">“Lorem ipsum dolor sit amet, consectetur adipiscing elit, sed do eiusmod tempor incididunt ut labore et dolore magna aliqua. Ut enim ad minim veniam, quis nostrud exercitation ullamco”</div>
    <div class="who" style="margin:6px 0 0 30px"><span class="avatar"></span>Mr &amp; Mrs Tarrow,</div>
  </div>
</section>

<footer class="sec footer">
  <div class="abs" style="left:75px;top:32px">
    <h6>Quick links</h6>
    <ul><li>Home</li><li>About Us</li><li>Products</li><li>News</li><li>Contacts</li></ul>
  </div>
  <div class="abs" style="left:202px;top:32px;width:230px">
    <h6>Contact information</h6>
    <p style="line-height:1.55">Lipovaya ul. 27, Brevno village,<br>Zarechny District, Moscow Region,<br>143990, Russia</p>
    <p style="margin-top:22px">+7 (495) 000 3 218</p>
    <p style="margin-top:22px">info@velmorix-hire.ru</p>
  </div>
  <div class="abs" style="left:478px;top:32px">
    <h6>Subscribe newsletter</h6>
    <p style="width:260px;line-height:1.5;margin-bottom:16px">Enter your email and receive latest offers &amp; news updates!</p>
    <div class="f-input">Name</div>
    <div class="f-input">Email</div>
    <span class="f-btn">Subscribe</span>
  </div>
  <div class="abs brand" style="left:75px;top:252px"><span class="brand-dot" style="background:#fff"></span><div><div class="brand-name" style="color:#fff">velmorix</div><div class="brand-sub" style="color:#ccc">crowd recruitment</div></div></div>
  <p class="abs" style="left:75px;top:318px;font-size:12px;line-height:1.6">© 2017 VELMORIX Crowd Recruitment .<br>Terms of Use &nbsp;|&nbsp; Privacy Policy</p>
  <div class="abs social" style="left:478px;top:320px"><h6 style="margin:0 8px 0 0">Follow us:</h6><span></span><span></span></div>
  <div class="abs feedback">
    <svg class="abs" style="left:-4px;top:-4px" width="44" height="56" viewBox="0 0 44 56"><path d="M0 0h44v56l-22-12L0 56z" fill="#3b7ccf"/><path d="M14 32l14-14 4 4-14 14h-4z" fill="#fff"/></svg>
    <h6>Feedback</h6>
    <div class="f-input">Name</div>
    <div class="f-input">Email</div>
    <div class="f-input" style="height:92px">Message</div>
    <div class="f-btn" style="display:block;text-align:center;margin-top:4px">Submit</div>
  </div>
</footer>

</body>
</html>
```